Chiropractor needs a snazzy business card

Business card for a chiropractic office.
Office treats patients of all ages.
Focus is on a natural lifestyle.
Colors can include the logo colors as well as white and a little orange.
Ideally the card would have something chiropractic related such as a spine.

The back of the card should have a items for making appointments (date, times....)

```html
<!DOCTYPE html>
<html lang="en">
<head>
<meta charset="utf-8">
<title>Meridian Chiropractic – Business Card</title>
<link href="https://fonts.googleapis.com/css2?family=Libre+Baskerville:wght@400;700&family=Roboto:wght@400&display=swap" rel="stylesheet">
<style>
  :root {
    --stage: #e9eaec;
    --card-green: #5cbb46;
    --card-white: #f6f6f6;
    --navy: #233b8c;
    --green: #4fae3a;
    --body-cyan: #5fe0f0;
    --body-blue: #2f8fc9;
    --rule: #7a7a7a;
    --label: #444;
  }
  * { margin: 0; padding: 0; box-sizing: border-box; }
  html, body { width: 1200px; height: 900px; overflow: hidden; }
  body {
    background: var(--stage);
    font-family: "Libre Baskerville", Georgia, serif;
    position: relative;
  }
  .card {
    position: absolute;
    left: 340px;
    width: 520px;
    height: 297px;
    border-radius: 2px;
    overflow: hidden;
    box-shadow: 0 6px 18px rgba(0,0,0,.18);
  }

  /* Appointment side */
  .card--appointment { top: 110px; background: var(--card-green); }
  .spine-art {
    position: absolute;
    left: 40px; top: 60px;
    width: 270px; height: 237px;
    background: radial-gradient(ellipse at 45% 55%, var(--body-cyan) 0%, var(--body-blue) 55%, rgba(47,143,201,0) 80%);
    border-radius: 45% 45% 0 0;
  }
  .brand--light {
    position: absolute;
    right: 24px; top: 22px;
    text-align: right;
    color: #fff;
  }
  .brand__name {
    display: block;
    font-size: 30px;
    letter-spacing: 2px;
    line-height: 1;
    text-transform: uppercase;
  }
  .brand__sub {
    display: block;
    font-size: 15px;
    letter-spacing: 4px;
    text-transform: uppercase;
    margin-top: 4px;
  }
  .appointment-box {
    position: absolute;
    right: 22px; top: 92px;
    width: 250px; height: 140px;
    background: #fff;
    border-radius: 8px;
    font-family: "Roboto", Arial, sans-serif;
    font-size: 8px;
    color: var(--label);
  }
  .appointment-box .line {
    position: absolute;
    height: 1px;
    background: var(--rule);
  }
  .appointment-box .label { position: absolute; }

  /* Contact side */
  .card--contact { top: 490px; background: var(--card-white); }
  .brand--dark {
    position: absolute;
    left: 36px; top: 40px;
    color: var(--navy);
  }
  .brand--dark .brand__name { font-size: 34px; }
  .brand--dark .brand__sub { font-size: 17px; letter-spacing: 4px; }
  .person {
    position: absolute;
    left: 36px; top: 196px;
  }
  .person__name { color: var(--navy); font-size: 20px; }
  .person__title { color: var(--green); font-size: 13px; margin-top: 2px; }
  .contact-list {
    position: absolute;
    left: 280px; top: 170px;
    list-style: none;
    color: var(--navy);
    font-size: 12px;
  }
  .contact-list li { display: flex; align-items: center; gap: 8px; height: 22px; }
  .contact-list .icon { width: 15px; height: 15px; flex: none; }
  .contact-list strong { color: var(--green); font-weight: 700; }
  .band {
    position: absolute;
    left: 0; right: 0; bottom: 0;
    height: 14px;
    background: var(--navy);
  }
</style>
</head>
<body>

<section class="card card--appointment">
  <div class="spine-art" role="img" aria-label="Illustration of a human back with the spine highlighted"></div>
  <div class="brand brand--light">
    <span class="brand__name">Meridian</span>
    <span class="brand__sub">Chiropractic</span>
  </div>
  <div class="appointment-box">
    <span class="line" style="left:20px;right:16px;top:28px"></span>
    <span class="label" style="left:98px;top:34px">appointment on</span>
    <span class="line" style="left:20px;right:16px;top:62px"></span>
    <span class="label" style="left:190px;top:66px">date</span>
    <span class="line" style="left:20px;right:16px;top:96px"></span>
    <span class="label" style="left:54px;top:100px">day</span>
    <span class="label" style="left:160px;top:100px">time</span>
  </div>
</section>

<section class="card card--contact">
  <div class="brand brand--dark">
    <span class="brand__name">Meridian</span>
    <span class="brand__sub">Chiropractic</span>
  </div>
  <div class="person">
    <p class="person__name">Clara Hensley</p>
    <p class="person__title">Title/Position</p>
  </div>
  <ul class="contact-list">
    <li>
      <svg class="icon" viewBox="0 0 16 16"><circle cx="8" cy="8" r="8" fill="var(--green)"/><rect x="5.5" y="3.5" width="5" height="9" rx="1" fill="none" stroke="#fff" stroke-width="1.2"/></svg>
      <span>123 555 0182</span>
    </li>
    <li>
      <svg class="icon" viewBox="0 0 16 16"><circle cx="8" cy="8" r="8" fill="var(--green)"/><rect x="4" y="5" width="8" height="6" fill="none" stroke="#fff" stroke-width="1.1"/><path d="M4 5l4 3.5L12 5" fill="none" stroke="#fff" stroke-width="1.1"/></svg>
      <span><strong>info</strong>@meridianchiro.com</span>
    </li>
    <li>
      <svg class="icon" viewBox="0 0 16 16"><circle cx="8" cy="8" r="8" fill="var(--green)"/><circle cx="8" cy="8" r="4.2" fill="none" stroke="#fff" stroke-width="1.1"/><path d="M3.8 8h8.4M8 3.8c-2 2.5-2 5.9 0 8.4M8 3.8c2 2.5 2 5.9 0 8.4" fill="none" stroke="#fff" stroke-width="0.9"/></svg>
      <span>www.meridianchiro.com</span>
    </li>
  </ul>
  <div class="band"></div>
</section>

</body>
</html>
```